Stickers to put on my honeyglasses

Stickers for my honey glasses.
Only a single sticker on the front. Same should have a stripe on the top side which goes above the lid to show if the glass was opened.
Size of the main part should be 55mm high and max. 100 mm wide.
The stripe on the top should be 70mm long.
I added a Picture of another producer which uses the same glass as I do.
I should say: 'e Maringer Glas Hunneg'. which means 'another glass of honey. 'Hunneg' should be mainly visible and therefore very large. 'e Maringer Glas' should be less visible and therefore smaller above the 'Hunneg'
- It needs to contain the quantity : '500gr'
- It needs to contain my Name and address: 'Jos Maringer, 14, rue Pierre Faber, L-7590 Miersch' (This should be small and not to visible)
- It needs to conatin a validity Line: ´Am beschte virum:` (With enough space so I can add a date by hand)
- It needs to say: 'dréchen, kill andäischterstockéieren' (to store it dry cold and dark)

```html
<!DOCTYPE html>
<html lang="lb">
<head>
<meta charset="utf-8">
<title>Hunneg – Glasetikett</title>
<link rel="stylesheet" href="https://fonts.googleapis.com/css2?family=Crimson+Pro:wght@700&family=Montserrat:wght@500;600;700&display=swap">
<style>
  :root {
    --page-bg: #fbf4e3;
    --frame-brown: #6b4423;
    --gold-light: #f7e27a;
    --gold-mid: #e2a63a;
    --gold-deep: #b9782a;
    --panel-top: #ffffff;
    --panel-bottom: #fcf0cf;
    --brand-red: #d53a40;
    --band-light: #a77a45;
    --band-dark: #4d2f17;
    --text-brown: #5a3a1e;
    --text-white: #ffffff;
    --field-border: #d9cbb0;
  }
  * { box-sizing: border-box; margin: 0; padding: 0; }
  html, body {
    width: 1200px; height: 1200px; overflow: hidden;
    background: var(--page-bg);
  }
  .canvas { position: relative; width: 1200px; height: 1200px; }

  /* Tamper seal strip running over the lid */
  .seal-strip {
    position: absolute; left: 470px; top: 44px;
    width: 260px; height: 618px;
    background: var(--frame-brown);
    border-radius: 10px 10px 0 0;
    z-index: 2;
  }
  .seal-strip__gold {
    position: absolute; left: 11px; right: 11px; top: 11px; bottom: 0;
    border-radius: 6px 6px 0 0;
    background: linear-gradient(90deg, var(--gold-deep) 0%, var(--gold-light) 50%, var(--gold-deep) 100%);
  }
  .seal-strip__paper {
    position: absolute; left: 25px; right: 25px; top: 25px; bottom: 0;
    border-radius: 3px 3px 0 0;
    background: var(--panel-top);
  }

  .label {
    position: absolute; left: 60px; top: 620px;
    width: 1080px; height: 453px;
    border-radius: 44px;
    background: var(--frame-brown);
  }
  .label__gold {
    position: absolute; inset: 11px;
    border-radius: 36px;
    background: linear-gradient(100deg, var(--gold-deep) 0%, var(--gold-light) 22%, var(--gold-mid) 45%, var(--gold-light) 70%, var(--gold-deep) 100%);
  }
  .label__panel {
    position: absolute; inset: 25px;
    border-radius: 24px;
    background: linear-gradient(180deg, var(--panel-top) 0%, var(--panel-top) 62%, var(--panel-bottom) 100%);
    overflow: hidden;
  }

  .floral { position: absolute; }
  .floral--left {
    left: 0; top: 0; width: 270px; height: 403px;
    background: radial-gradient(ellipse at 45% 60%, #f1e2c0 0%, #f8efd9 55%, rgba(255,255,255,0) 100%);
  }
  .floral--right {
    right: 0; top: 0; width: 210px; height: 270px;
    background: radial-gradient(ellipse at 60% 45%, #f1e2c0 0%, #f8efd9 55%, rgba(255,255,255,0) 100%);
  }

  .kicker {
    position: absolute; left: 0; right: 0; top: 42px;
    text-align: center;
    font-family: "Montserrat", Arial, sans-serif;
    font-weight: 600; font-size: 22px; letter-spacing: 0.5px;
    color: var(--text-brown);
  }
  .brand-name {
    position: absolute; left: 0; right: 0; top: 80px;
    text-align: center;
    padding-left: 4px;
    font-family: "Crimson Pro", "Times New Roman", serif;
    font-weight: 700; font-size: 124px; line-height: 1;
    letter-spacing: 3px;
    color: var(--brand-red);
  }

  .divider { position: absolute; left: 357px; top: 224px; width: 317px; height: 16px; }

  .info-band {
    position: absolute; left: 220px; top: 273px;
    width: 810px; height: 45px;
    background: linear-gradient(90deg, var(--band-light) 0%, #8a5e31 35%, var(--band-dark) 100%);
  }
  .storage-note {
    position: absolute; right: 24px; top: 0; line-height: 45px;
    font-family: "Montserrat", Arial, sans-serif;
    font-weight: 600; font-size: 14px;
    color: var(--text-white);
  }

  .quantity {
    position: absolute; left: 0; width: 1030px; top: 336px;
    text-align: center;
    font-family: "Montserrat", Arial, sans-serif;
    font-weight: 700; font-size: 20px;
    color: var(--text-brown);
  }
  .best-before {
    position: absolute; right: 24px; top: 326px;
    font-family: "Montserrat", Arial, sans-serif;
    font-weight: 600; font-size: 11px;
    color: var(--text-brown);
  }
  .date-field {
    position: absolute; left: 823px; top: 346px;
    width: 184px; height: 42px;
    background: var(--panel-top);
    border: 1px solid var(--field-border);
    border-radius: 4px;
  }
  .date-field::after {
    content: ""; position: absolute; left: 12px; right: 12px; bottom: 8px;
    border-bottom: 2px dotted var(--gold-deep);
  }
  .address {
    position: absolute; left: 0; width: 1030px; top: 378px;
    text-align: center;
    font-family: "Montserrat", Arial, sans-serif;
    font-weight: 600; font-size: 10px;
    color: var(--text-brown);
  }
</style>
</head>
<body>
<main class="canvas">
  <div class="seal-strip" aria-hidden="true">
    <div class="seal-strip__gold"></div>
    <div class="seal-strip__paper"></div>
  </div>

  <section class="label">
    <div class="label__gold"></div>
    <div class="label__panel">
      <div class="floral floral--left" role="img" aria-label="Fine gold line illustration of daisies and honeycomb"></div>
      <div class="floral floral--right" role="img" aria-label="Fine gold line illustration of flowers and honeycomb cells"></div>

      <p class="kicker">e Maringer Glas</p>
      <h1 class="brand-name">HUNNEG</h1>

      <svg class="divider" viewBox="0 0 317 16" aria-hidden="true">
        <defs>
          <linearGradient id="dividerGold" x1="0" x2="1" y1="0" y2="0">
            <stop offset="0" stop-color="#c98a2e"/>
            <stop offset="0.5" stop-color="#f7e27a"/>
            <stop offset="1" stop-color="#c98a2e"/>
          </linearGradient>
        </defs>
        <rect x="6" y="6" width="305" height="4" rx="2" fill="url(#dividerGold)"/>
        <ellipse cx="9" cy="8" rx="9" ry="7" fill="url(#dividerGold)"/>
        <ellipse cx="308" cy="8" rx="9" ry="7" fill="url(#dividerGold)"/>
      </svg>

      <div class="info-band">
        <p class="storage-note">dréchen, kill andäischterstockéieren</p>
      </div>

      <p class="quantity">500g</p>
      <p class="best-before">Am beschte virum:</p>
      <div class="date-field"></div>
      <p class="address">Jos Maringer, 14, rue Pierre Faber, L-7590 Miersch</p>
    </div>
  </section>
</main>
</body>
</html>
```